Moderne CI für einen Immobilienmakler [www.brekow-immobilien.de]
Zielgruppe
Kunden für hochwertige Immobilien, also gemischtes eher anspruchvolles Klientel.
Hallo,
ich betreibe ein junges Immobilienunternehmen im 4. Geschäftsjahr. Wir vermarkten ausschließlich hochwertige Immobilien. Meine derzeitiges Logo habe ich damals selbst entworfen und es harmoniert gut mit meiner Website [www.brekow-immobilien.de] leider habe ich für Printmedien nie eine CI hinbekommen die mir richtig gefällt und die im Gesamt- und Farbkonzept zu meinem Onlineauftritt passt.
Ich wünsche mir nun von einem professionellen Designer eine modern- edle CI mit Entwürfen für Briefpapier, Umschläge C4 und DL, A4 Exposé-Mappe sowie die Rohlinge für eine Dreiseiter Image-Broschüre, für ein Objekt Expose sowie für eine Print-Annonce.
Eine spätere Zusammenarbeit für weitere Medien ist erwünscht.

```html
<!DOCTYPE html>
<html lang="de">
<head>
<meta charset="utf-8">
<title>Visitenkarte Brekow Immobilien</title>
<link rel="stylesheet" href="https://fonts.googleapis.com/css2?family=Arimo:wght@400&family=PT+Sans:wght@400&display=swap">
<style>
  :root {
    --bg: #ffffff;
    --card: #ffffff;
    --ink: #111111;
    --label: #8a8a8a;
    --line: #222222;
    --note-edge: #d8d8d8;
  }
  * { margin: 0; padding: 0; box-sizing: border-box; }
  html, body { width: 1200px; height: 1200px; overflow: hidden; background: var(--bg); }
  .canvas { position: relative; width: 1200px; height: 1200px; font-family: "Arimo", Arial, sans-serif; color: var(--ink); }

  .card {
    position: absolute; width: 808px; height: 540px; background: var(--card);
    border: 1px solid #cfcfcf; box-shadow: 0 4px 14px rgba(0,0,0,0.22);
  }
  .card--front { left: 40px; top: 42px; }
  .card--back { left: 170px; top: 612px; }

  .name { position: absolute; font-size: 56px; line-height: 1; letter-spacing: -0.5px; }
  .role { position: absolute; font-size: 25px; line-height: 1; }
  .brand {
    position: absolute; color: var(--ink); line-height: 1; white-space: nowrap;
    font-family: "Arimo", Arial, sans-serif; font-weight: 400;
  }
  .address { position: absolute; font-family: "PT Sans", Verdana, sans-serif; font-size: 29px; line-height: 37px; }
  .phones { position: absolute; font-family: "PT Sans", Verdana, sans-serif; font-size: 22px; line-height: 28px; }
  .web { position: absolute; font-family: "PT Sans", Verdana, sans-serif; font-size: 22px; line-height: 28px; text-align: right; }

  /* Front */
  .card--front .name { left: 34px; top: 34px; }
  .card--front .role { left: 36px; top: 94px; }
  .card--front .brand { left: 388px; top: 170px; font-size: 46px; }
  .card--front .address { left: 36px; top: 218px; }
  .card--front .phones { left: 36px; top: 430px; }
  .card--front .web { right: 42px; top: 430px; }

  /* Back */
  .card--back .name { left: 36px; top: 28px; }
  .card--back .brand { left: 240px; top: 28px; font-size: 56px; }
  .card--back .role { left: 38px; top: 88px; }
  .card--back .address { left: 36px; top: 170px; }
  .card--back .phones { left: 36px; top: 404px; }
  .card--back .web { right: 42px; top: 430px; }

  .appointment-note {
    position: absolute; left: 468px; top: 142px; width: 226px; height: 222px;
    background: #fbfbfb; border: 1px solid var(--note-edge);
    box-shadow: 0 3px 8px rgba(0,0,0,0.15);
    font-size: 22px; text-align: center; padding: 30px 18px 0;
  }
  .appointment-note__tape {
    position: absolute; left: 78px; top: -10px; width: 70px; height: 22px;
    background: #e6e6e6; opacity: 0.85;
  }
  .appointment-note__field { height: 92px; }
  .appointment-note__label { display: block; margin-bottom: 30px; }
  .appointment-note__line { display: block; height: 1px; background: var(--line); }

  .side-label {
    position: absolute; color: var(--label); letter-spacing: 0;
    writing-mode: vertical-rl; transform: rotate(180deg); line-height: 1;
  }
  .side-label--front { left: 872px; top: 42px; height: 540px; font-size: 72px; }
  .side-label--back { left: 1000px; top: 612px; height: 540px; font-size: 76px; }
</style>
</head>
<body>
<div class="canvas">

  <section class="card card--front" aria-label="Vorderseite">
    <div class="name">Henrik Brekow</div>
    <div class="role">Geschäftsführer</div>
    <div class="brand">brekow immobilien</div>
    <div class="address">Lindenhofweg 14<br>35039 Marburg<br>Deutschland</div>
    <div class="phones">Telefon: +49 (0)6421-5520417<br>Telefax: +49 (0)6421-5520419</div>
    <div class="web">info@brekow-immobilien.de<br>www.brekow-immobilien.de</div>
  </section>
  <div class="side-label side-label--front">VORDERSEITE</div>

  <section class="card card--back" aria-label="Rückseite">
    <div class="name">Henrik</div>
    <div class="brand">brekow immobilien</div>
    <div class="role">Geschäftsführer</div>
    <div class="address">Lindenhofweg 14<br>35039 Marburg<br>Deutschland</div>
    <div class="appointment-note">
      <span class="appointment-note__tape"></span>
      <div class="appointment-note__field">
        <span class="appointment-note__label">Termin am:</span>
        <span class="appointment-note__line"></span>
      </div>
      <div class="appointment-note__field">
        <span class="appointment-note__label">Uhrzeit:</span>
        <span class="appointment-note__line"></span>
      </div>
    </div>
    <div class="phones">Telefon: +49 (0)6421-5520417<br>Telefax: +49 (0)6421-5520419</div>
    <div class="web">info@brekow-immobilien.de<br>www.brekow-immobilien.de</div>
  </section>
  <div class="side-label side-label--back">RÜCKSEITE</div>

</div>
</body>
</html>
```